Tallow Electrical Business Card

We need a business card design for our family-run electrical contracting business based in Western Australia called 'Tallow Electrical'. We provide electrical services including residential, commercial and industrial. We aim for individual business cards to be made for all of our employees. We already have a company logo, which we require to be featured on the design. We would like simple, sleek and vibrant designs, which incorporate our logo and represent our business. We do not want anything involving too many graphics/images. We like the colours red, black, white and all shades of grey. The final design should communicate professionalism and trustworthiness.
We require the following contact information:
Name- Peter Hargreave
EC 5810
Mobile number- 0455 902 318
Fax number (including area code)- (08) 9576 2083
Email adress- name@tallowelectric.com.au
Industry/Entity Type
Electrical
Font styles to use
Other font styles liked:
- ITC Handel Bold
Look and feel

```html
<!DOCTYPE html>
<html lang="en">
<head>
<meta charset="utf-8">
<title>Tallow Electrical Business Card</title>
<link href="https://fonts.googleapis.com/css2?family=Arimo:wght@400;700&display=swap" rel="stylesheet">
<style>
  :root {
    --red: #e32227;
    --red-deep: #b3161b;
    --black: #231f20;
    --grey-dark: #4a4a4a;
    --grey-mid: #9a9a9a;
    --grey-light: #e6e6e6;
    --white: #ffffff;
    --stage: #d9d9d9;
  }
  * { margin: 0; padding: 0; box-sizing: border-box; }
  html, body { width: 1200px; height: 900px; overflow: hidden; }
  body {
    background: var(--stage);
    font-family: "Arimo", Arial, sans-serif;
    position: relative;
  }
  .card {
    position: absolute;
    left: 300px;
    width: 600px;
    height: 360px;
    box-shadow: 0 6px 18px rgba(0,0,0,.18);
    overflow: hidden;
  }
  /* Back side */
  .card-back {
    top: 50px;
    background: radial-gradient(ellipse at 45% 35%, #ee3a3e 0%, var(--red) 45%, var(--red-deep) 100%);
    display: flex;
    align-items: center;
    justify-content: center;
  }
  .brand {
    display: flex;
    align-items: center;
    gap: 12px;
    font-weight: 700;
    letter-spacing: 1px;
    text-transform: uppercase;
  }
  .brand-mark { width: 22px; height: 22px; }
  .card-back .brand { color: var(--white); font-size: 30px; }
  .card-back .brand-mark { background: var(--white); }

  /* Front side */
  .card-front {
    top: 480px;
    background: var(--white);
  }
  .card-front .brand {
    position: absolute;
    top: 48px;
    right: 46px;
    color: var(--black);
    font-size: 24px;
  }
  .card-front .brand-mark { background: var(--red); width: 18px; height: 18px; }
  .holder-name {
    position: absolute;
    top: 118px;
    left: 128px;
    color: var(--red);
    font-weight: 700;
    font-size: 19px;
  }
  .divider {
    position: absolute;
    top: 150px;
    left: 296px;
    width: 2px;
    height: 70px;
    background: linear-gradient(var(--white), var(--grey-light), var(--white));
  }
  .licence {
    position: absolute;
    left: 12px;
    top: 208px;
    font-size: 10px;
    color: var(--grey-dark);
  }
  .band-red {
    position: absolute;
    left: 0; top: 226px;
    width: 282px; height: 14px;
    background: var(--red);
  }
  .band-black {
    position: absolute;
    left: 292px; top: 262px;
    width: 308px; height: 14px;
    background: var(--black);
  }
  .contact {
    position: absolute;
    top: 128px;
    left: 326px;
    list-style: none;
    font-size: 12.5px;
    line-height: 1.35;
    color: var(--grey-dark);
  }
  .contact li { display: flex; align-items: flex-start; gap: 10px; margin-bottom: 3px; }
  .contact svg { width: 11px; height: 12px; margin-top: 2px; flex: none; fill: var(--red); }
  .contact .email { padding-left: 21px; }
</style>
</head>
<body>
  <section class="card card-back" aria-label="Card back">
    <div class="brand"><span class="brand-mark"></span><span>Tallow Electrical</span></div>
  </section>

  <section class="card card-front" aria-label="Card front">
    <div class="brand"><span class="brand-mark"></span><span>Tallow Electrical</span></div>
    <p class="holder-name">Peter Hargreave</p>
    <div class="divider"></div>
    <ul class="contact">
      <li>
        <svg viewBox="0 0 12 14"><path d="M6 0a5 5 0 0 0-5 5c0 3.5 5 9 5 9s5-5.5 5-9a5 5 0 0 0-5-5zm0 7a2 2 0 1 1 0-4 2 2 0 0 1 0 4z"/></svg>
        <span>EC 5810, address<br>town here 6542U</span>
      </li>
      <li>
        <svg viewBox="0 0 12 14"><path d="M2 0h8v14H2zM3.5 1.5v9h5v-9z"/></svg>
        <span>0455 902 318</span>
      </li>
      <li>
        <svg viewBox="0 0 12 14"><path d="M1 5h10v7H1zM3 1h6v3H3z"/></svg>
        <span>(08) 9576 2083</span>
      </li>
      <li class="email">name@tallowelectric.com.au</li>
    </ul>
    <p class="licence">EC 7402</p>
    <div class="band-red"></div>
    <div class="band-black"></div>
  </section>
</body>
</html>
```